Pebble Ledger WEB application

We need a small webdesign for a WEB-Application. Functionality will be provided by our developers. All we need are templates with HTML5, CSS and Java functionality for the "animated" parts. As well as some images and logos .
See attached Powerpoint. Please ignore last slide.
Design should be state of the art material design as know from Quorvix or Zelpad latest OS versions
In the end will be fluid design (fitting automatically to actual screen size) but template should base on 540 x 960

Target Market(s)

UK Mobile Market

Number of Pages Required

5+ page

Font styles to use
Sans Serif

Requirements
Must have
• next to requierements in Powerpoint we need animations as stated in PP (progress animation).
Nice to have
• All textfiles should be in a XML file to be easily translated to other languages.Can be done by our developers as well

```html
<!DOCTYPE html>
<html lang="en">
<head>
<meta charset="utf-8">
<title>Pebble Ledger – Attention</title>
<link rel="stylesheet" href="https://fonts.googleapis.com/css2?family=Roboto:wght@400;500;700&display=swap">
<style>
  :root {
    --page-bg: #ffffff;
    --panel-bg: #2c2d2f;
    --header-bg: #353638;
    --deep-bg: #111111;
    --footer-bg: #242527;
    --divider: #4a4b4d;
    --text-light: #f2f2f2;
    --text-muted: #d6d6d6;
    --accent-green: #3ff12c;
    --button-top: #2cc222;
    --button-bottom: #178f12;
    --alert-red: #ff2a2a;
  }
  * { box-sizing: border-box; margin: 0; padding: 0; }
  html, body {
    width: 800px; height: 1200px; overflow: hidden;
    background: var(--page-bg);
    font-family: "Roboto", sans-serif;
  }
  .screen {
    position: absolute; left: 128px; top: 120px;
    width: 544px; height: 960px;
    background: var(--panel-bg);
    box-shadow: 0 2px 10px rgba(0,0,0,0.25);
    display: flex; flex-direction: column;
  }
  .screen-header {
    height: 125px; background: var(--header-bg);
    display: flex; align-items: center; justify-content: space-between;
    padding: 0 30px 0 30px;
    color: var(--text-light); font-size: 30px;
  }
  .info-icon { width: 46px; height: 46px; }
  .status-line {
    height: 62px; display: flex; align-items: center; justify-content: center;
    color: var(--text-light); font-size: 24px;
    border-bottom: 2px solid var(--divider);
  }
  .battery-zone {
    height: 285px; background: var(--deep-bg);
    display: flex; flex-direction: column; align-items: center;
    padding-top: 40px;
  }
  .battery-icon { width: 80px; height: 140px; }
  .battery-message {
    margin-top: 40px; color: var(--text-muted); font-size: 24px;
  }
  .battery-message .gain { color: var(--alert-red); }
  .action-zone {
    flex: 1; display: flex; flex-direction: column; align-items: center;
    padding-top: 43px;
  }
  .cta-button {
    width: 442px; height: 80px; border-radius: 40px;
    background: linear-gradient(var(--button-top), var(--button-bottom));
    color: #fff; font-weight: 700; font-size: 21px; letter-spacing: 0.5px;
    display: flex; align-items: center; justify-content: center;
    box-shadow: 0 2px 4px rgba(0,0,0,0.4);
  }
  .tagline {
    margin-top: 28px; color: var(--text-light); font-size: 31px;
  }
  .save-ring {
    margin-top: 28px; width: 190px; height: 190px; border-radius: 50%;
    border: 6px solid var(--accent-green);
    display: flex; flex-direction: column; align-items: center; justify-content: center;
    color: var(--accent-green);
  }
  .save-ring .value { font-size: 46px; font-weight: 500; line-height: 1; }
  .save-ring .label { font-size: 24px; margin-top: 6px; }
  .screen-footer {
    height: 72px; background: var(--footer-bg);
    display: flex; align-items: center; justify-content: center;
    color: var(--text-muted); font-size: 23px;
  }
</style>
</head>
<body>
  <main class="screen">
    <header class="screen-header">
      <h1 style="font-size:inherit;font-weight:400">Attention</h1>
      <svg class="info-icon" viewBox="0 0 46 46" aria-label="Info">
        <circle cx="23" cy="23" r="20" fill="none" stroke="#d6d6d6" stroke-width="3"/>
        <rect x="21.5" y="19" width="3" height="15" fill="#d6d6d6"/>
        <circle cx="23" cy="13.5" r="2" fill="#d6d6d6"/>
      </svg>
    </header>
    <p class="status-line">Several Battery Drainers found</p>
    <section class="battery-zone">
      <svg class="battery-icon" viewBox="0 0 80 140" aria-label="Low battery">
        <rect x="26" y="0" width="28" height="10" fill="#3ff12c"/>
        <rect x="0" y="10" width="80" height="76" fill="#3ff12c"/>
        <rect x="2" y="10" width="76" height="128" fill="none" stroke="#3ff12c" stroke-width="4"/>
        <rect x="37" y="26" width="6" height="32" fill="#111"/>
        <rect x="37" y="64" width="6" height="7" fill="#111"/>
      </svg>
      <p class="battery-message">Your battery could last <span class="gain">XY%</span> longer</p>
    </section>
    <section class="action-zone">
      <div class="cta-button">START FREE OPTIMIZATION NOW</div>
      <p class="tagline">World premiere web technology</p>
      <div class="save-ring">
        <span class="value">100%</span>
        <span class="label">Save</span>
      </div>
    </section>
    <footer class="screen-footer">No download needed, no access rights</footer>
  </main>
</body>
</html>
```